Varnell Skyworks Limited

Started a consulting business 12 months ago and have since moved location and have grown and seek to identify my self to the industry.
Specializing in quality solutions, business documentation and maintenance solution's

Industry/Entity Type

Business

```html
<!DOCTYPE html>
<html lang="en">
<head>
<meta charset="utf-8">
<title>Varnell Skyworks Limited – Business Card</title>
<link rel="stylesheet" href="https://fonts.googleapis.com/css2?family=Crimson+Text:ital,wght@0,600;1,600&family=Della+Respira&display=swap">
<style>
  :root {
    --backdrop: #ece8e2;
    --card: #0a0b0d;
    --rule: #1f3f41;
    --company: #9b9b9b;
    --name-gold: #c99a42;
    --detail: #f4f4f4;
  }
  html, body {
    margin: 0;
    width: 1200px;
    height: 1000px;
    overflow: hidden;
    background: var(--backdrop);
  }
  .canvas {
    position: relative;
    width: 1200px;
    height: 1000px;
  }
  .card {
    position: absolute;
    left: 222px;
    top: 269px;
    width: 756px;
    height: 456px;
    background: var(--card);
    overflow: hidden;
  }
  .rule {
    position: absolute;
    right: 0;
    height: 3px;
    background: var(--rule);
  }
  .rule--company { top: 116px; width: 349px; }
  .rule--name { top: 203px; width: 565px; }
  .rule--divider { top: 293px; left: 0; width: 756px; }

  .company-name {
    position: absolute;
    right: 36px;
    top: 72px;
    margin: 0;
    font-family: "Crimson Text", serif;
    font-weight: 600;
    font-size: 31px;
    line-height: 1;
    color: var(--company);
    white-space: nowrap;
  }
  .person-name {
    position: absolute;
    left: 246px;
    top: 150px;
    margin: 0;
    font-family: "Crimson Text", serif;
    font-style: italic;
    font-weight: 600;
    font-size: 42px;
    line-height: 1;
    color: var(--name-gold);
    white-space: nowrap;
  }
  .details {
    font-family: "Della Respira", serif;
    font-size: 22px;
    color: var(--detail);
    font-style: normal;
  }
  .address {
    position: absolute;
    left: 79px;
    top: 326px;
    line-height: 38px;
  }
  .address-line { display: block; white-space: nowrap; }
  .icon {
    position: absolute;
    fill: var(--detail);
  }
  .icon--home { left: 41px; top: 318px; }
  .icon--phone { left: 451px; top: 328px; }
  .icon--mail { left: 451px; top: 384px; }
  .phone {
    position: absolute;
    left: 478px;
    top: 334px;
    white-space: nowrap;
  }
  .email {
    position: absolute;
    left: 489px;
    top: 383px;
    white-space: nowrap;
  }
</style>
</head>
<body>
<main class="canvas">
  <section class="card">
    <h1 class="company-name">Varnell Skyworks Limited</h1>
    <div class="rule rule--company"></div>

    <h2 class="person-name">Daniel R Hale</h2>
    <div class="rule rule--name"></div>

    <div class="rule rule--divider"></div>

    <svg class="icon icon--home" width="28" height="32" viewBox="0 0 28 32" aria-hidden="true">
      <path d="M14 0 L28 12 L0 12 Z"/>
      <path d="M2 14 H26 V32 H2 Z M6 19 V24 H13 V19 Z" fill-rule="evenodd"/>
    </svg>
    <address class="details address">
      <span class="address-line">Unit B204, 18 Kestrel Lane</span>
      <span class="address-line">Northfield 2016</span>
      <span class="address-line">Auckland NZ</span>
    </address>

    <svg class="icon icon--phone" width="24" height="34" viewBox="0 0 24 34" aria-hidden="true">
      <path d="M9 2 C4 4 1 10 2 18 C3 25 7 31 12 33 L15 28 C11 26 8 22 8 17 C8 12 10 9 13 8 Z"/>
      <path d="M10 1 L15 0 L18 7 L14 9 Z"/>
    </svg>
    <div class="details phone">+64 21 555 014</div>

    <svg class="icon icon--mail" width="30" height="18" viewBox="0 0 30 18" aria-hidden="true">
      <rect x="0" y="0" width="30" height="18"/>
      <path d="M1 1 L15 11 L29 1" fill="none" stroke="#0a0b0d" stroke-width="1.6"/>
    </svg>
    <div class="details email">hello@varnellsky.co.nz</div>
  </section>
</main>
</body>
</html>
```